Boutique Recruiting Firm Needs Eye-Catching Business Cards (and potentially new logo)!

I run a recruiting company in Charleston, South Carolina. I have a ton of networking events coming up and need business cards to grab potential clients attention.

I currently have a logo but if you want to try and recreate the logo to something more modern I am open to that. If you do decide to create a new logo please submit the business card with the old logo and the new one.

Staffing Beyond the Lantern, LLC is the name of my company. I create videos to my clients and candidates which allows me to standout from my competition so I would like a business card (and possibly new logo) to do the same.

I do not specialize in any one industry of recruiting.

Industry/Entity Type

Business

```html
<!DOCTYPE html>
<html lang="en">
<head>
<meta charset="utf-8">
<title>Staffing Beyond the Lantern, LLC — Business Cards</title>
<link rel="stylesheet" href="https://fonts.googleapis.com/css2?family=Open+Sans:wght@400;600;700&display=swap">
<style>
  :root {
    --brand-blue: #1f7cc4;
    --brand-blue-light: #3a93d6;
    --brand-blue-dark: #1666a8;
    --card-white: #ffffff;
    --divider-grey: #7d8185;
    --stage-bg: #eceef0;
    --faint-mark: rgba(255,255,255,0.14);
  }
  * { box-sizing: border-box; margin: 0; padding: 0; }
  html, body {
    width: 1200px; height: 900px; overflow: hidden;
    background: var(--stage-bg);
    font-family: "Open Sans", Arial, sans-serif;
  }
  .stage { position: relative; width: 1200px; height: 900px; }

  .card {
    position: absolute;
    width: 560px; height: 320px;
    overflow: hidden;
    box-shadow: 0 10px 30px rgba(0,0,0,0.18);
  }

  /* Back of card */
  .card-back {
    left: 90px; top: 90px;
    background: linear-gradient(135deg, var(--brand-blue-light), var(--brand-blue) 55%, var(--brand-blue-dark));
  }
  .card-back .faint-mark {
    position: absolute; left: 40px; top: 60px;
    width: 200px; height: 200px; border-radius: 50%;
    background: var(--faint-mark);
  }
  .card-back .wordmark {
    position: absolute; right: 36px; top: 112px;
    text-align: right; color: var(--card-white);
    font-weight: 600; line-height: 1.1;
  }
  .wordmark .line-main { display: block; font-size: 38px; }
  .wordmark .line-sub { display: block; font-size: 22px; }

  /* Front of card */
  .card-front {
    left: 550px; top: 490px;
    background: var(--card-white);
  }
  .card-front .wave { position: absolute; left: 0; top: 0; width: 560px; height: 320px; }
  .card-front .brand {
    position: absolute; left: 0; right: 0; top: 46px;
    display: flex; align-items: center; justify-content: center; gap: 16px;
  }
  .brand .brand-dot {
    width: 54px; height: 54px; border-radius: 50%;
    background: var(--brand-blue);
  }
  .card-front .wordmark {
    color: var(--brand-blue); font-weight: 600; line-height: 1.1;
  }
  .card-front .wordmark .line-main { font-size: 36px; }
  .card-front .wordmark .line-sub { font-size: 21px; }

  .contact {
    position: absolute; left: 0; right: 0; top: 208px;
    color: var(--card-white); text-align: center;
    font-size: 15px; line-height: 1.75;
  }
  .contact .person-name { font-weight: 700; font-size: 17px; }
  .contact .person-role { font-size: 14px; }
  .contact .sep { margin: 0 6px; }
  .contact svg { width: 13px; height: 13px; vertical-align: -2px; margin-right: 4px; fill: none; stroke: var(--card-white); stroke-width: 2; }
</style>
</head>
<body>
<main class="stage">

  <section class="card card-back" aria-label="Business card back">
    <div class="faint-mark"></div>
    <div class="wordmark">
      <span class="line-main">Staffing Beyond</span>
      <span class="line-sub">the Lantern, LLC</span>
    </div>
  </section>

  <section class="card card-front" aria-label="Business card front">
    <svg class="wave" viewBox="0 0 560 320" preserveAspectRatio="none">
      <path d="M0 196 C150 160 330 150 560 190 L560 320 L0 320 Z" fill="#9a9ea2"/>
      <path d="M0 202 C150 166 330 156 560 196 L560 320 L0 320 Z" fill="var(--brand-blue)"/>
    </svg>

    <div class="brand">
      <span class="brand-dot"></span>
      <div class="wordmark">
        <span class="line-main">Staffing Beyond</span>
        <span class="line-sub">the Lantern, LLC</span>
      </div>
    </div>

    <div class="contact">
      <div><span class="person-name">Dana Whitfield</span><span class="sep">•</span><span class="person-role">Manager</span></div>
      <div>
        <svg viewBox="0 0 24 24"><path d="M5 3h4l2 5-3 2a12 12 0 0 0 6 6l2-3 5 2v4a2 2 0 0 1-2 2A18 18 0 0 1 3 5a2 2 0 0 1 2-2z"/></svg>555 014 2398
        <span class="sep"></span>
        <svg viewBox="0 0 24 24"><circle cx="12" cy="12" r="9"/><path d="M3 12h18M12 3c3 3 3 15 0 18M12 3c-3 3-3 15 0 18"/></svg>www.danawhitfield.com
      </div>
      <div>@ dana@whitfieldmail.com</div>
    </div>
  </section>

</main>
</body>
</html>
```